Universität sucht Plakat-Design zur Werbung
Zielgruppe
Universität Lindbrück-Hagenau; Plakat zur Werbung für eine Schülerveranstaltungsreihe / Studieninteressierte (gymnasiale Oberstufe)
Aufgabenstellung
Plakat in
DIN A1 → von A1 auf A5 verkleinerbar (auf Schriftgröße achten)
Titel: Probierhochschule Informatik 2018
Folgende Texte sollen wörtlich auf dem Plakat erscheinen:
'Vorträge von Mitarbeitern und Studierenden zu unterschiedlichen Themen aus der Informatik: Visualisierung, Virtual Reality & Augmented Reality, Software Engineering uvm.! Abgerundet wird der Tag durch den Einblick in eine echte Vorlesung sowie einer Gesprächsrunde mit Studierenden und Informatikern aus der Praxis.
Wann: Dienstag, 30. Oktober 2018, ab 9 Uhr
Wo: Universität Lindbrück-Hagenau, Campus Nordstadt, Kieselhalle (K07 E00 S03)
Der Eintritt ist frei. Eine Anmeldung ist erforderlich unter: http://ulh-beispiel.de/probierhochschule'
Anforderungen an das Design:
- Fähnchen/Marke: „Veranstaltung für Schüler und Lehrer“
- Text und Uni- sowie FTW-Logo verwenden
- modern, jugendlich
- zeitlos / für mehrere Jahre verwendbar (Zur Erklärung: Die Probierhochschule soll zukünftig einmal jährlich stattfinden und das Grunddesign soll in den nächsten Jahren wieder verwendet werden können.)
- Informatiksymbolik, ggf. Begriffe aus der Informatik
- aufmerksamkeitserregend bzw. auffällig (zB durch passende Farbwahl/Motiv)
- abstrakte Visualisierung (im Hintergrund)
- nicht zu technisch; keine Bilder von konkreter Technik (wie zB einem Computer)
Wir benötigen alle Dateien (editierbar Grafikdatei (zB InDesign), Bilder usw.), um in zukünftigen Jahren das Plakat anpassen zu können.

```html
<!DOCTYPE html>
<html lang="de">
<head>
<meta charset="utf-8">
<title>Probierhochschule Informatik 2018</title>
<link rel="stylesheet" href="https://fonts.googleapis.com/css2?family=Jost:wght@500;600;700&display=swap">
<style>
  :root {
    --backdrop: #f0b2a8;
    --red-deep: #c8323f;
    --red: #e2503f;
    --orange: #ee7448;
    --accent-blue: #004c93;
    --white: #ffffff;
    --info-panel: rgba(214, 150, 160, 0.85);
  }
  * { margin: 0; padding: 0; box-sizing: border-box; }
  html, body { width: 1200px; height: 1200px; overflow: hidden; background: var(--backdrop); }
  body { font-family: "Jost", "Futura", sans-serif; }

  .poster {
    position: absolute; left: 219px; top: 60px;
    width: 762px; height: 1079px; overflow: hidden;
    box-shadow: 4px 6px 10px rgba(90, 30, 40, 0.3);
  }
  .poster__backdrop {
    position: absolute; inset: 0;
    background:
      radial-gradient(circle at 20% 30%, rgba(240,130,70,0.7), transparent 45%),
      radial-gradient(circle at 85% 80%, rgba(160,30,60,0.6), transparent 50%),
      linear-gradient(160deg, var(--orange) 0%, var(--red) 45%, var(--red-deep) 100%);
  }

  .rule { position: absolute; height: 6px; background: var(--white); }
  .rule--top { left: 0; top: 55px; width: 597px; }
  .rule--bottom { left: 165px; top: 211px; right: 0; }

  .title { position: absolute; right: 215px; top: 68px; text-align: right; color: var(--white); font-weight: 600; line-height: 1; }
  .title__event { display: block; font-size: 50px; letter-spacing: -0.5px; }
  .title__subject { display: block; font-size: 90px; letter-spacing: -1px; margin-top: -4px; }
  .title__year {
    position: absolute; left: 558px; top: 92px;
    writing-mode: vertical-rl; color: var(--accent-blue);
    font-size: 36px; font-weight: 700; line-height: 1; letter-spacing: 1px;
  }

  .lead { position: absolute; left: 40px; top: 320px; width: 682px; text-align: center; }
  .lead__line {
    display: inline-block; background: var(--white); color: var(--accent-blue);
    font-size: 28px; font-weight: 700; line-height: 1.15; padding: 0 3px; margin-bottom: 6px;
  }

  .topics {
    position: absolute; left: 40px; top: 414px; width: 682px;
    text-align: center; color: var(--white);
    font-size: 22px; font-weight: 600; line-height: 30px; letter-spacing: 0.3px;
  }

  .detail { position: absolute; left: 51px; color: var(--white); font-size: 28px; font-weight: 600; line-height: 36px; }
  .detail--when { top: 716px; }
  .detail--where { top: 787px; }
  .detail__label {
    position: absolute; left: 0; top: 2px;
    background: var(--white); color: var(--accent-blue);
    font-weight: 600; font-size: 27px; line-height: 30px; padding: 0 5px;
  }
  .detail__value { margin-left: 119px; display: block; white-space: nowrap; }

  .footer { position: absolute; left: 35px; top: 956px; right: 0; height: 96px; display: flex; }
  .brand {
    width: 251px; display: flex; align-items: center; gap: 12px; padding-right: 10px;
  }
  .brand__square { width: 22px; height: 22px; background: var(--white); flex: none; }
  .brand__name { color: var(--white); font-size: 19px; font-weight: 600; line-height: 24px; }
  .registration {
    flex: 1; background: var(--info-panel); color: var(--accent-blue);
    font-size: 21px; font-weight: 600; line-height: 30px; padding: 2px 14px;
  }
</style>
</head>
<body>
  <div class="poster">
    <div class="poster__backdrop" role="img" aria-label="Abstrakte Low-Poly-Fläche aus roten und orangen Dreiecken"></div>

    <div class="rule rule--top"></div>
    <h1 class="title">
      <span class="title__event">Probierhochschule</span>
      <span class="title__subject">Informatik</span>
    </h1>
    <div class="title__year">2018</div>
    <div class="rule rule--bottom"></div>

    <div class="lead">
      <span class="lead__line">Vorträge von Mitarbeitern und Studierenden zu</span>
      <span class="lead__line">unterschiedlichen Themen aus der Informatik</span>
    </div>

    <p class="topics">
      Visualisierung, Virtual Reality &amp; Augmented Reality,<br>
      Software Engineering uvm.!<br>
      Abgerundet wird der Tag durch den<br>
      Einblick in eine echte Vorlesung sowie einer<br>
      Gesprächsrunde mit Studierenden und<br>
      Informatikern aus der Praxis.
    </p>

    <div class="detail detail--when">
      <span class="detail__label">Wann:</span>
      <span class="detail__value">Dienstag, 30. Oktober 2018, ab 9 Uhr</span>
    </div>
    <div class="detail detail--where">
      <span class="detail__label">Wo:</span>
      <span class="detail__value">Universität Lindbrück-Hagenau,</span>
      <span class="detail__value">Campus Nordstadt, Kieselhalle (K07 E00 S03)</span>
    </div>

    <div class="footer">
      <div class="brand">
        <span class="brand__square"></span>
        <span class="brand__name">Universität Lindbrück-Hagenau</span>
      </div>
      <div class="registration">
        Der Eintritt ist frei.<br>
        Eine Anmeldung ist erforderlich unter:<br>
        http://ulh-beispiel.de/probierhochschule
      </div>
    </div>
  </div>
</body>
</html>
```